I would love for my business card to be fun and sophisicated. The clients are people that could afford nice well crafted wigs. These wigs are not like granny wigs. The're for women who are stylish and what to look there best especially if they are dealing with cancer are some from of hair loss. Do not want the card to appear crowded with to much information. If I need to eliminate some data, let me know.
Thanks

Industry/Entity Type

Hair

Contact Information for Business Card

L Radiant Tresses, Marjorie Ellison, owner, stylist

Wigs/Studio Showroom
Extensions
Hair Replacement
Private Room

24683 Mesa Vista Loop, Suite. R
Irvine, CA 90871
(949) 555-0178
Email: tresses@lradianttresses-example.com
www.lradianttresses-example.com

```html
<!DOCTYPE html>
<html lang="en">
<head>
<meta charset="utf-8">
<title>L Radiant Tresses — Business Card</title>
<link rel="stylesheet" href="https://fonts.googleapis.com/css2?family=Poppins:wght@400;500;600&display=swap">
<style>
  :root {
    --page-bg: #ffffff;
    --card-bg: #f1efee;
    --card-bg-soft: #e6e3e2;
    --brand-red: #e2383b;
    --ink: #161616;
    --band-black: #0d0d0d;
    --band-black-soft: #262626;
    --wig-brown: #6b3a22;
    --wig-dark: #2a1c16;
    --wig-bg: #ebe8e6;
  }
  * { box-sizing: border-box; margin: 0; padding: 0; }
  html, body {
    width: 1200px;
    height: 900px;
    overflow: hidden;
    background: var(--page-bg);
  }
  body {
    position: relative;
    font-family: "Poppins", "Century Gothic", sans-serif;
    color: var(--ink);
  }
  .business-card {
    position: absolute;
    left: 100px;
    top: 164px;
    width: 1000px;
    height: 572px;
    border-radius: 36px;
    overflow: hidden;
    background: radial-gradient(ellipse at 60% 40%, var(--card-bg) 0%, var(--card-bg-soft) 100%);
    border: 1px solid #dedad8;
  }
  .brand-name {
    position: absolute;
    left: 54px;
    top: 48px;
    font-size: 66px;
    font-weight: 500;
    line-height: 1;
    color: var(--brand-red);
    letter-spacing: -0.5px;
    white-space: nowrap;
  }
  .owner {
    position: absolute;
    left: 56px;
    top: 186px;
  }
  .owner-name {
    font-size: 28px;
    font-weight: 600;
    color: var(--brand-red);
    line-height: 1.2;
  }
  .owner-role {
    font-size: 24px;
    font-weight: 400;
    line-height: 1.3;
  }
  .address, .contact {
    position: absolute;
    left: 56px;
    font-style: normal;
    font-size: 24px;
    line-height: 1.3;
    white-space: nowrap;
  }
  .address { top: 278px; }
  .contact { top: 362px; }
  .wig-showcase {
    position: absolute;
    left: 620px;
    top: 250px;
    width: 350px;
    height: 230px;
    display: flex;
    gap: 14px;
  }
  .wig-photo {
    flex: 1;
    border-radius: 10px 10px 0 0;
  }
  .wig-photo--bob {
    background: radial-gradient(ellipse at 50% 35%, var(--wig-brown) 0%, #8d5a3e 45%, var(--wig-bg) 80%);
  }
  .wig-photo--long {
    background: radial-gradient(ellipse at 50% 45%, var(--wig-dark) 0%, #4a3128 50%, var(--wig-bg) 85%);
  }
  .service-band {
    position: absolute;
    left: 0;
    top: 480px;
    width: 100%;
    height: 30px;
    background: var(--brand-red);
    display: flex;
    align-items: center;
    justify-content: center;
    font-size: 17px;
    font-weight: 500;
    letter-spacing: 7px;
    color: var(--ink);
    white-space: nowrap;
  }
  .base-band {
    position: absolute;
    left: 0;
    top: 510px;
    width: 100%;
    height: 62px;
    background: linear-gradient(180deg, var(--band-black-soft) 0%, var(--band-black) 100%);
  }
</style>
</head>
<body>
  <article class="business-card">
    <h1 class="brand-name">L Radiant Tresses</h1>

    <div class="owner">
      <p class="owner-name">Marjorie Ellison</p>
      <p class="owner-role">owner/stylist</p>
    </div>

    <address class="address">
      24683 Mesa Vista Loop Ste. R<br>
      Irvine, CA 90871
    </address>

    <address class="contact">
      (949) 555-0178<br>
      www.lradianttresses-example.com<br>
      tresses@lradianttresses-example.com
    </address>

    <div class="wig-showcase">
      <div class="wig-photo wig-photo--bob" role="img" aria-label="Photo of an auburn bob wig with bangs on a display head"></div>
      <div class="wig-photo wig-photo--long" role="img" aria-label="Photo of a long dark brown wig on a display head"></div>
    </div>

    <div class="service-band">studio showroom Hair Replacement Extensions</div>
    <div class="base-band"></div>
  </article>
</body>
</html>
```